Brisk Fixwell business card

I need business card for my business, I think you have all my details.six months ago I design with you car wrap design. We would like to design both side of the card. On front of card we would like logo , Name and our contact details.
At the back we are looking to mentioned our services.
The name will be:
Farzadullah Korimi
Managing Director
Ph:07843529176
Email:info@brisk-fixwell.com
Web:www.brisk-fixwell.com
So we have our logo, you don’t need to change the logo.
Please see the attachment.
Thanks

Target Market(s)

Home improvement

Industry/Entity Type

Home Improvement

Contact Information for Business Card

Company name: Brisk Fixwell
Name: Farzadullah Korimi
Position: Director
Ph:07843529176
Web: www.brisk-fixwell.com
Add: 42 Larkfield Crescent
Hounslow
TW3 9LB
SECOND PERSON
Nasirudin korimi
Position: Handyman
Ph: 07712 634508
Email: info@brisk-fixwell.com
Add: 18 Wrenmoor Park Lane
Hounslow
TW6 2QJ

```html
<!DOCTYPE html>
<html lang="en">
<head>
<meta charset="utf-8">
<title>Brisk Fixwell – Business Card</title>
<link rel="stylesheet" href="https://fonts.googleapis.com/css2?family=Roboto:wght@400;500;700;900&display=swap">
<style>
  :root {
    --stage: #e9e4de;
    --card-white: #f7f7f8;
    --navy: #2b3282;
    --ink-light: #e6e8f4;
    --shadow: rgba(40, 30, 20, 0.18);
  }
  * { margin: 0; padding: 0; box-sizing: border-box; }
  html, body {
    width: 1200px;
    height: 1054px;
    overflow: hidden;
    background: var(--stage);
    font-family: "Roboto", Arial, sans-serif;
  }
  .canvas {
    width: 1200px;
    height: 1054px;
    display: flex;
    align-items: center;
    justify-content: center;
  }
  .business-card {
    position: relative;
    width: 900px;
    height: 542px;
    border-radius: 16px;
    overflow: hidden;
    background: var(--card-white);
    box-shadow: 0 18px 40px var(--shadow);
  }
  .brand-area {
    position: absolute;
    left: 63px;
    top: 48px;
  }
  .brand-name {
    font-weight: 700;
    font-size: 64px;
    line-height: 1;
    letter-spacing: 0.5px;
    color: var(--navy);
  }
  .info-band {
    position: absolute;
    left: 0;
    right: 0;
    top: 233px;
    bottom: 0;
    background: var(--navy);
  }
  .holder {
    position: absolute;
    left: 63px;
    top: 52px;
    color: #ffffff;
  }
  .holder-name {
    font-weight: 500;
    font-size: 28px;
    line-height: 1.2;
  }
  .holder-title {
    margin-top: 6px;
    font-weight: 400;
    font-size: 20px;
    color: var(--ink-light);
  }
  .contact-list {
    position: absolute;
    left: 73px;
    top: 162px;
    list-style: none;
  }
  .contact-item {
    display: flex;
    align-items: center;
    height: 34px;
    font-size: 20px;
    color: var(--ink-light);
  }
  .contact-icon {
    width: 18px;
    height: 18px;
    margin-right: 16px;
    flex: none;
  }
  .brand-mark {
    position: absolute;
    left: 520px;
    top: 172px;
    width: 300px;
    height: 300px;
    border-radius: 50%;
    background: var(--card-white);
    border: 14px solid var(--navy);
    box-shadow: 0 0 0 6px var(--card-white);
  }
</style>
</head>
<body>
  <main class="canvas">
    <section class="business-card" aria-label="Brisk Fixwell business card, front">
      <div class="brand-area">
        <div class="brand-name">Brisk Fixwell</div>
      </div>

      <div class="info-band">
        <div class="holder">
          <h1 class="holder-name">Farzadullah Korimi</h1>
          <p class="holder-title">Managing Director</p>
        </div>

        <ul class="contact-list">
          <li class="contact-item">
            <svg class="contact-icon" viewBox="0 0 24 24" aria-hidden="true">
              <path fill="#e6e8f4" d="M3 8c0-2 4-4 9-4s9 2 9 4v2h-5V8H8v2H3z"/>
              <path fill="#e6e8f4" d="M6 12h12l2 8H4z"/>
              <circle cx="12" cy="16" r="2" fill="#2b3282"/>
            </svg>
            07843529176
          </li>
          <li class="contact-item">
            <svg class="contact-icon" viewBox="0 0 24 24" aria-hidden="true">
              <rect x="2" y="5" width="20" height="14" fill="#e6e8f4"/>
              <path d="M2 5l10 8 10-8" fill="none" stroke="#2b3282" stroke-width="2"/>
            </svg>
            info@brisk-fixwell.com
          </li>
          <li class="contact-item">
            <svg class="contact-icon" viewBox="0 0 24 24" aria-hidden="true">
              <circle cx="12" cy="12" r="10" fill="#e6e8f4"/>
              <g fill="none" stroke="#2b3282" stroke-width="1.5">
                <ellipse cx="12" cy="12" rx="4" ry="10"/>
                <path d="M2 12h20M4 7h16M4 17h16"/>
              </g>
            </svg>
            www.brisk-fixwell.com
          </li>
        </ul>
      </div>

      <div class="brand-mark" role="img" aria-label="Brisk Fixwell brand mark area"></div>
    </section>
  </main>
</body>
</html>
```